Virtual assistant company needs letterhead and email signature

We need a letterhead and email signature for our virtual assistant company - taskBeaver (small w capital F). Our tag line is plan ahead | taskBeaver

The colours we would like used are;

#81788c
#dddbe1

For reference our business cards have used #81788c background colour and #dddbe1 text

The fonts we would like used are

Lora
Proxima Nova

Please check out our twitter and facebook for style and feel

Twitter: @taskbeaver
www.examplebook.test/taskbeaver

Please also find attached our landing page and business cards for reference

Any questions please let us know

Thanks
E

Reason: We like the opportunity to receive furthur designs

```html
<!DOCTYPE html>
<html lang="en">
<head>
<meta charset="utf-8">
<title>taskBeaver Letterhead</title>
<link href="https://fonts.googleapis.com/css2?family=Figtree:wght@300;400&display=swap" rel="stylesheet">
<style>
  :root {
    --brand: #81788c;
    --brand-light: #dddbe1;
    --paper: #ffffff;
    --ink: #1e1e22;
    --backdrop: #e4e3e7;
    --signature-tone: #ecebee;
  }
  * { box-sizing: border-box; margin: 0; padding: 0; }
  html, body {
    width: 1200px;
    height: 900px;
    overflow: hidden;
    background: var(--backdrop);
  }
  .letterhead {
    position: absolute;
    left: 322px;
    top: 58px;
    width: 556px;
    height: 784px;
    background: var(--paper);
    font-family: "Figtree", "Helvetica Neue", Arial, sans-serif;
    color: var(--ink);
  }
  .letterhead__header {
    height: 80px;
    background: var(--brand);
    display: flex;
    align-items: center;
    justify-content: space-between;
    padding: 0 30px 0 23px;
    color: var(--brand-light);
    font-weight: 300;
  }
  .brand-name {
    font-size: 24px;
    letter-spacing: 0.3px;
  }
  .tagline {
    font-size: 13px;
    letter-spacing: 0.3px;
  }
  .letter {
    position: absolute;
    left: 80px;
    top: 155px;
    width: 396px;
  }
  .letter__subject {
    font-size: 12px;
    line-height: 15px;
    margin-bottom: 38px;
  }
  .letter__body p {
    font-size: 9.9px;
    line-height: 12.6px;
    letter-spacing: 0.12px;
    text-align: justify;
    hyphens: auto;
    margin-bottom: 13px;
  }
  .signature {
    position: absolute;
    left: 80px;
    top: 608px;
    width: 110px;
    height: 38px;
    background: var(--signature-tone);
  }
  .letterhead__footer {
    position: absolute;
    left: 0;
    bottom: 0;
    width: 100%;
    height: 52px;
    background: var(--brand);
    display: flex;
    align-items: center;
    padding-left: 23px;
    gap: 30px;
  }
  .social {
    display: flex;
    align-items: center;
    gap: 8px;
    font-size: 10px;
    color: var(--brand-light);
  }
  .social__dot {
    width: 22px;
    height: 22px;
    border-radius: 50%;
    background: var(--brand-light);
  }
</style>
</head>
<body>
  <article class="letterhead">
    <header class="letterhead__header">
      <span class="brand-name">taskBeaver</span>
      <span class="tagline">plan ahead | taskBeaver</span>
    </header>

    <section class="letter">
      <p class="letter__subject">Lorem ipsum<br>dolor sit amet</p>
      <div class="letter__body">
        <p>Lorem ipsum dolor sit amet, consectetuer adipiscing elit. Nam nibh. Nunc varius facilisis eros. Sed erat. In in velit quis arcu ornare laoreet. Curabitur adipiscing luctus massa. Integer ut purus ac augue commodo commodo. Nunc nec mi eu justo tempor consectetuer. Etiam vitae nisl. In dignissim lacus ut ante. Cras elit lectus, bibendum a, adipiscing vitae, commodo et, dui. Ut tincidunt tortor. Donec nonummy, enim in lacinia pulvinar, velit tellus scelerisque augue, ac posuere libero urna eget neque. Cras ipsum. Vestibulum pretium, lectus nec venenatis volutpat, purus lectus ultrices risus, a condimentum risus mi et quam. Pellentesque auctor fringilla neque. Duis eu massa ut lorem iaculis vestibulum. Maecenas facilisis elit sed justo. Quisque volutpat malesuada velit.</p>
        <p>Nunc at velit quis lectus nonummy eleifend. Curabitur eros. Aenean ligula dolor, gravida auctor, auctor et, suscipit in, erat. Sed malesuada, enim ut congue pharetra, massa elit convallis pede, ornare scelerisque libero neque ut neque. In at libero. Curabitur molestie. Sed vel neque. Proin et dolor ac ipsum elementum malesuada. Praesent id orci. Donec hendrerit. In hac habitasse platea dictumst. Aenean sit amet arcu a turpis posuere pretium.</p>
        <p>Nulla mauris odio, vehicula in, condimentum sit amet, tempus id, metus. Donec at nisi sit amet felis blandit posuere. Aliquam erat volutpat. Cras lobortis orci in quam porttitor cursus. Aenean dignissim. Curabitur facilisis sem at nisi laoreet placerat. Duis sed ipsum ac nibh mattis feugiat. Proin sed purus. Vivamus lectus ipsum, rhoncus sed, scelerisque sit amet, ultrices in, dolor. Aliquam vel magna non nunc ornare bibendum. Sed libero. Maecenas at est. Vivamus ornare, felis et luctus dapibus, lacus leo convallis diam, eget dapibus augue arcu eget arcu.</p>
      </div>
    </section>

    <div class="signature" role="img" aria-label="Handwritten signature of the sender"></div>

    <footer class="letterhead__footer">
      <span class="social"><span class="social__dot"></span>taskbeaver</span>
      <span class="social"><span class="social__dot"></span>@taskbeaver</span>
    </footer>
  </article>
</body>
</html>
```